Brindlecote Roofing Business Card

Need a business card with the logo that was designed here

Contact Information for Business Card

Name, Title, Phone, Email, Website, Company name

```html
<!DOCTYPE html>
<html lang="en">
<head>
<meta charset="utf-8">
<title>Brindlecote Roofing Business Card</title>
<link href="https://fonts.googleapis.com/css2?family=Open+Sans:wght@400;600;700&display=swap" rel="stylesheet">
<style>
  :root {
    --backdrop: #4a4a4a;
    --card-white: #ffffff;
    --brand-blue: #1b75bd;
    --brand-blue-deep: #1462a3;
    --swoosh-grey: #939598;
    --ink: #2b2b2b;
  }
  * { margin: 0; padding: 0; box-sizing: border-box; }
  html, body {
    width: 1200px; height: 801px; overflow: hidden;
    background: var(--backdrop);
    font-family: "Open Sans", Arial, sans-serif;
  }
  .stage {
    position: relative; width: 1200px; height: 801px;
    display: flex; align-items: center; justify-content: center; gap: 48px;
  }
  .card {
    position: relative; width: 525px; height: 300px;
    border-radius: 16px; overflow: hidden;
  }
  .card-front { background: var(--card-white); }
  .card-back { background: var(--brand-blue); display: flex; align-items: center; justify-content: center; }

  .swoosh { position: absolute; inset: 0; width: 100%; height: 100%; }

  .front-brand {
    position: absolute; left: 34px; top: 0; bottom: 0; width: 200px;
    display: flex; align-items: center; gap: 10px;
  }
  .brand-mark { width: 14px; height: 14px; background: var(--brand-blue); flex: none; }
  .brand-name {
    font-weight: 700; font-size: 23px; line-height: 1.15; color: var(--brand-blue);
  }
  .divider {
    position: absolute; left: 245px; top: 48px; width: 1.5px; height: 190px;
    background: var(--brand-blue);
  }
  .contact {
    position: absolute; left: 262px; top: 50px; color: var(--ink);
    font-size: 12.5px; line-height: 1.35;
  }
  .contact-name { font-weight: 700; font-size: 19px; color: var(--brand-blue); line-height: 1.1; letter-spacing: 0.3px; }
  .contact-title { font-size: 12.5px; margin-bottom: 16px; }
  .contact-address { margin-bottom: 16px; }
  .contact-line { display: flex; align-items: center; gap: 6px; }
  .contact-line svg { width: 11px; height: 11px; flex: none; }

  .back-brand { display: flex; align-items: center; gap: 16px; }
  .back-brand .brand-mark { width: 22px; height: 22px; background: var(--brand-blue-deep); }
  .back-brand .brand-name { font-size: 40px; color: var(--brand-blue-deep); white-space: nowrap; }
</style>
</head>
<body>
<main class="stage">
  <section class="card card-front" aria-label="Card front">
    <svg class="swoosh" viewBox="0 0 525 300" preserveAspectRatio="none" aria-hidden="true">
      <path d="M485 0 H525 V300 H420 C450 200 470 90 485 0 Z" fill="var(--swoosh-grey)"/>
      <path d="M385 300 C420 230 445 190 472 150 C455 200 434 250 410 300 Z" fill="var(--brand-blue)"/>
    </svg>

    <div class="front-brand">
      <span class="brand-mark"></span>
      <span class="brand-name">Brindlecote<br>Roofing</span>
    </div>

    <div class="divider"></div>

    <div class="contact">
      <p class="contact-name">DANA WHITLOCK</p>
      <p class="contact-title">Managing Director</p>
      <p class="contact-address">Your address, City<br>State, Zip 1234</p>
      <p class="contact-line">
        <svg viewBox="0 0 12 12"><path d="M3 1 L5 3.5 L4 5 Q5.5 7 7 8 L8.5 7 L11 9 L9.5 11 Q4 10 1 2.5 Z" fill="var(--brand-blue)"/></svg>
        123 456 789
      </p>
      <p class="contact-line">
        <svg viewBox="0 0 12 12"><rect x="1" y="2.5" width="10" height="7" fill="var(--brand-blue)"/><path d="M1 2.5 L6 6.5 L11 2.5" stroke="#fff" fill="none"/></svg>
        info@yourmail.com
      </p>
      <p class="contact-line">
        <svg viewBox="0 0 12 12"><circle cx="6" cy="6" r="5" fill="var(--brand-blue)"/><path d="M1 6 H11 M6 1 Q3 6 6 11 M6 1 Q9 6 6 11" stroke="#fff" stroke-width="0.8" fill="none"/></svg>
        www.yourwebsite.com
      </p>
    </div>
  </section>

  <section class="card card-back" aria-label="Card back">
    <div class="back-brand">
      <span class="brand-mark"></span>
      <span class="brand-name">Brindlecote Roofing</span>
    </div>
  </section>
</main>
</body>
</html>
```